Heater product information sheets

I need the two product information sheets organized and laid out in a clean, easy to read attractive manner. These sheets are to advertise propane heaters for outdoor use and for wholesale to propane distributors, restaurants and homeowners that need to have propane heat as the winter ends and spring begins. They will be used for chilly evenings when people want to be outside eating, drinking and being social.
Updates

Low design quality

Target Market(s)

Restaurants, hospitality industry, special events, party rental companies, home owners with backyards

Font styles to use
Sans Serif

Requirements
Must have
• My logo in the document instead of k. Dahlby and company
Nice to have
• I would like to see Fire illustrated coming up the heaters and on the round glass, show it up the middle of the glass tube propane heater.

```html
<!DOCTYPE html>
<html lang="en">
<head>
<meta charset="utf-8">
<title>Propane Outdoor Heaters – Dahlby &amp; Company</title>
<link rel="stylesheet" href="https://fonts.googleapis.com/css2?family=Arimo:wght@400;700&family=Noto+Serif:wght@400;700&display=swap">
<style>
  :root {
    --charcoal: #33332f;
    --ink: #3b4454;
    --orange: #e69a40;
    --paper: #f4f4f4;
    --white: #ffffff;
    --text: #2d2d2d;
    --footer: #3a3128;
  }
  * { margin: 0; padding: 0; box-sizing: border-box; }
  html, body { width: 848px; height: 1200px; overflow: hidden; }
  body { background: var(--paper); font-family: "Arimo", Arial, sans-serif; color: var(--text); }
  .sheet { position: relative; width: 848px; height: 1200px; overflow: hidden; }
  .abs { position: absolute; }

  /* Header */
  .hero { left: 0; top: 0; width: 848px; height: 245px; background: var(--charcoal); }
  .hero-photo { left: 400px; top: 0; width: 448px; height: 245px;
    background: linear-gradient(90deg, rgba(51,51,47,1) 0%, rgba(80,84,70,.85) 25%, #6b6f5a 55%, #8b8e7c 80%, #a4a394 100%); }
  .hero-rule { left: 0; top: 245px; width: 848px; height: 7px; background: var(--orange); }
  .hero-title { left: 50px; top: 36px; font-family: "Noto Serif", serif; font-weight: 400; color: var(--white); font-size: 38px; line-height: 1; }
  .hero-heaters { left: 50px; top: 90px; font-family: "Noto Serif", serif; font-weight: 700; color: var(--orange); font-size: 60px; line-height: 1; letter-spacing: 1px; }
  .hero-sub { left: 51px; top: 162px; color: var(--white); font-size: 21px; line-height: 26px; }
  .hero-offers { left: 452px; top: 166px; list-style: none; color: var(--white); font-weight: 700; font-size: 11.5px; letter-spacing: .6px; line-height: 20px; }
  .hero-offers li::before { content: "●"; font-size: 8px; margin-right: 8px; vertical-align: 2px; }

  /* Product blocks */
  .product-name { font-weight: 700; font-size: 28px; line-height: 1; color: var(--ink); }
  .product-name .accent { color: var(--orange); }
  .product-heater { font-weight: 700; font-size: 60px; line-height: 1; color: var(--orange); letter-spacing: -1px; }
  .frame-accent { background: var(--orange); }
  .frame { background: var(--white); border: 1.5px solid var(--ink); }
  .product-shot { background: linear-gradient(180deg, #d8d8d6 0%, #9a9a98 30%, #3a3a3a 70%, #151515 100%); border-radius: 6px; }
  .label { background: var(--orange); color: var(--white); font-weight: 700; padding: 2px 5px; line-height: 1.15; }
  .note-label { font-size: 15px; }
  .note-text { font-size: 12.5px; line-height: 20px; color: #3d3d3d; width: 190px; }
  .note-text strong { color: var(--orange); }
  .section-label { font-size: 16.5px; letter-spacing: .2px; }
  .spec-list { list-style: none; font-size: 16px; line-height: 20px; color: var(--text); }
  .spec-list li { padding-left: 11px; text-indent: -11px; }
  .spec-list li::before { content: "●"; font-size: 9px; margin-right: 3px; vertical-align: 2px; }
  .spec-list .indent { padding-left: 13px; text-indent: 0; }
  .spec-list .indent::before { content: none; }
  .divider { left: 12px; top: 680px; width: 824px; height: 1.5px; background: var(--ink); }

  /* Footer */
  .cta { left: 28px; top: 1087px; font-family: "Noto Serif", serif; font-weight: 700; font-size: 19px; line-height: 1.1; color: var(--orange); }
  .footer { left: 0; top: 1110px; width: 848px; height: 90px;
    background: linear-gradient(100deg, #45382c 0%, var(--footer) 45%, #2f2822 100%); }
  .company { left: 46px; top: 1117px; font-family: "Noto Serif", serif; color: var(--white); font-size: 19px; letter-spacing: .5px; }
  .contact { left: 24px; font-family: "Noto Serif", serif; color: var(--white); font-size: 13.5px; display: flex; align-items: center; gap: 10px; }
  .contact.address { top: 1139px; font-weight: 700; }
  .contact.email { top: 1159px; }
  .phone { left: 395px; top: 1122px; display: flex; align-items: center; gap: 22px; color: var(--white); }
  .phone-number { font-weight: 700; font-size: 52px; line-height: 1; letter-spacing: .5px; }
</style>
</head>
<body>
<div class="sheet">

  <header>
    <div class="abs hero"></div>
    <div class="abs hero-photo" role="img" aria-label="Photograph of a patio heater standing among palm plants beside a garden fence"></div>
    <div class="abs hero-rule"></div>
    <h1>
      <span class="abs hero-title">Propane outdoor</span>
      <span class="abs hero-heaters">HEATERS</span>
    </h1>
    <p class="abs hero-sub">for wholesale to propane distributors,<br>restaurants and homeowners</p>
    <ul class="abs hero-offers">
      <li>RENTALS FOR LIVE EVENTS</li>
      <li>RENTALS FOR RESTAURANTS &amp; CATERING &nbsp;HALLS</li>
      <li>PURCHASE FOR YOUR HOME &nbsp;OR BUSINESS</li>
    </ul>
  </header>

  <!-- Outdoor propane heater -->
  <section>
    <h2>
      <span class="abs product-name" style="left:35px;top:268px;"><span class="accent">Outdoor</span> Propane</span>
      <span class="abs product-heater" style="left:34px;top:297px;">HEATER</span>
    </h2>
    <div class="abs frame-accent" style="left:19px;top:451px;width:125px;height:215px;"></div>
    <div class="abs frame" style="left:33px;top:364px;width:305px;height:289px;"></div>
    <div class="abs product-shot" style="left:44px;top:376px;width:76px;height:262px;" role="img" aria-label="Product photo of a black standing outdoor propane patio heater with a silver reflector top"></div>
    <span class="abs label note-label" style="left:129px;top:518px;">NOTE</span>
    <p class="abs note-text" style="left:131px;top:549px;">Price: Starting at <strong>$250</strong> each Assembly &amp; Delivery available upon request Discounts for large quantity orders</p>

    <span class="abs label section-label" style="left:362px;top:281px;">SPECIFICATIONS</span>
    <ul class="abs spec-list" style="left:364px;top:313px;">
      <li>Powerful 48,000 BTU</li>
      <li>Black Powder Coated Finish</li>
      <li>Uses 20 lbs. Propane Tank</li>
      <li>CE, GS, AGA, CSA, with ETL certificate and ROHS approved.</li>
    </ul>
    <span class="abs label section-label" style="left:362px;top:408px;">ADDITIONAL DETAILS</span>
    <ul class="abs spec-list" style="left:364px;top:440px;">
      <li>Commercial Quality</li>
      <li>For Outdoor Use Only</li>
      <li>Conforms to ANSI STD Z83.26-2014 Certified to CSA STD</li>
      <li class="indent">2.37-2014 Gas- fired outdoor infrared patio heaters</li>
      <li>&nbsp;Safety Auto Shut Off Switch</li>
      <li>Thermostatic Control</li>
      <li>Base Diameter 17” - Anti-Tip Design</li>
      <li>Standard Wheels - Tilt &amp; Move</li>
      <li>Run time: 8-10 hours with standard 20 lbs. Propane tank</li>
      <li>88” Tall</li>
      <li>Heating Area: 200 sq. ft</li>
    </ul>
  </section>

  <div class="abs divider"></div>

  <!-- Glass tube propane heater -->
  <section>
    <span class="abs label section-label" style="left:24px;top:703px;">SPECIFICATIONS</span>
    <ul class="abs spec-list" style="left:26px;top:735px;">
      <li>Powerful 48,000 BTU</li>
      <li>Black Powder Coated Finish</li>
      <li>Uses 20 lbs. Propane Tank</li>
      <li>CE, GS, AGA, CSA, with ETL certificate and ROHS approved.</li>
    </ul>
    <span class="abs label section-label" style="left:24px;top:829px;">ADDITIONAL DETAILS</span>
    <ul class="abs spec-list" style="left:26px;top:861px;">
      <li>Commercial Quality</li>
      <li>For Outdoor Use Only</li>
      <li>Conforms to ANSI STD Z83.26-2014 Certified to CSA STD</li>
      <li class="indent">2.37-2014 Gas- fired outdoor infrared patio heaters</li>
      <li>&nbsp;Safety Auto Shut Off Switch</li>
      <li>Thermostatic Control</li>
      <li>Base Diameter 17” - Anti-Tip Design</li>
      <li>Standard Wheels - Tilt &amp; Move</li>
      <li>Run time: 8-10 hours with standard 20 lbs. Propane tank</li>
      <li>88” Tall</li>
      <li>Heating Area: 200 sq. ft</li>
    </ul>

    <h2>
      <span class="abs product-name" style="left:520px;top:697px;"><span class="accent">Glass Tube</span>&nbsp; Propane</span>
      <span class="abs product-heater" style="left:520px;top:726px;">HEATER</span>
    </h2>
    <div class="abs frame-accent" style="left:508px;top:879px;width:125px;height:213px;"></div>
    <div class="abs frame" style="left:522px;top:792px;width:305px;height:288px;"></div>
    <div class="abs product-shot" style="left:533px;top:812px;width:76px;height:248px;" role="img" aria-label="Product photo of a black glass tube propane patio heater with a silver reflector top"></div>
    <span class="abs label note-label" style="left:618px;top:946px;">NOTE</span>
    <p class="abs note-text" style="left:620px;top:977px;">Price: Starting at <strong>$250</strong> each Assembly &amp; Delivery available upon request Discounts for large quantity orders</p>
  </section>

  <!-- Footer -->
  <footer>
    <div class="abs footer"></div>
    <p class="abs cta">To Rent or Purchase:</p>
    <p class="abs company">DAHLBY &amp; COMPANY</p>
    <p class="abs contact address">
      <svg width="12" height="14" viewBox="0 0 12 14" aria-hidden="true"><path d="M6 0a5 5 0 0 0-5 5c0 3.6 5 9 5 9s5-5.4 5-9a5 5 0 0 0-5-5zm0 7a2 2 0 1 1 0-4 2 2 0 0 1 0 4z" fill="#fff"/></svg>
      42 Orchard Ave Linden Falls, NJ 07000
    </p>
    <p class="abs contact email">
      <svg width="13" height="10" viewBox="0 0 13 10" aria-hidden="true"><rect x=".5" y=".5" width="12" height="9" fill="none" stroke="#fff"/><path d="M.5.5 6.5 6l6-5.5M.5 9.5l4.5-4.5M12.5 9.5 8 5" fill="none" stroke="#fff"/></svg>
      hello@dahlbyrentals.com
    </p>
    <div class="abs phone">
      <svg width="40" height="40" viewBox="0 0 24 24" aria-hidden="true"><path fill="#fff" d="M6.6 10.8a15.1 15.1 0 0 0 6.6 6.6l2.2-2.2c.3-.3.7-.4 1-.2 1.1.4 2.3.6 3.6.6.6 0 1 .4 1 1V20c0 .6-.4 1-1 1A17 17 0 0 1 3 4c0-.6.4-1 1-1h3.5c.6 0 1 .4 1 1 0 1.3.2 2.5.6 3.6.1.3 0 .7-.2 1z"/></svg>
      <span class="phone-number">555-204-3817</span>
    </div>
  </footer>

</div>
</body>
</html>
```